E-commerce website for interior joinery product - Furnvale Trade

we want to create a E-commerce website to list our modular products.
other than E-commerce functions, we will also require membership logins and setting different price tiers for B2B customers (construction company and home building groups. for logos and our products etc please visit www.furnvale.co.nz
You can also get some ideas from https://brontecabinets.co.nz/ready-to-order/

Number of Pages Required

5+ page

Requirements
Must have
• on the product page, the customer can have the option to choose different colours and upgradable options.

```html
<!DOCTYPE html>
<html lang="en">
<head>
<meta charset="utf-8">
<title>Furnvale – Wardrobe &amp; Door Systems</title>
<link href="https://fonts.googleapis.com/css2?family=Quicksand:wght@400;500;600;700&family=Lato:wght@400;700&display=swap" rel="stylesheet">
<style>
:root{
  --slate:#4d666d;
  --slate-dark:#3f565c;
  --heading:#5b6266;
  --text:#5f6468;
  --muted:#9aa0a3;
  --tab:#e4e6e7;
  --band:#e8e9ea;
  --card:#ebeced;
  --white:#ffffff;
  --footer:#263238;
  --footer-text:#8c979c;
}
*{box-sizing:border-box;margin:0;padding:0}
html,body{width:1200px;height:4721px;overflow:hidden;background:var(--white)}
body{position:relative;font-family:'Lato',sans-serif;color:var(--text)}
.abs{position:absolute}
h2.section-title{position:absolute;left:0;width:1200px;text-align:center;font-family:'Quicksand',sans-serif;font-weight:500;font-size:32px;color:var(--heading)}

/* header */
.site-header{position:absolute;left:0;top:0;width:1200px;height:99px;background:var(--white)}
.brand{position:absolute;left:143px;top:20px;display:flex;align-items:center;gap:12px}
.brand-mark{width:56px;height:56px;background:var(--slate)}
.brand-name{font-family:'Quicksand',sans-serif;font-weight:500;font-size:40px;color:var(--slate)}
.member-btn{position:absolute;left:793px;top:16px;width:162px;height:30px;background:#d6d9da;color:var(--slate);font-size:12px;display:flex;align-items:center;justify-content:center;gap:6px;font-family:'Lato',sans-serif}
.header-icon{position:absolute;top:19px}
.main-nav{position:absolute;top:65px;left:0;width:1200px;font-family:'Quicksand',sans-serif;font-size:14px;font-weight:500;color:var(--slate)}
.main-nav span{position:absolute}

/* hero */
.hero{position:absolute;left:0;top:99px;width:1200px;height:515px;background:linear-gradient(90deg,#b8a998 0%,#cfc2b3 30%,#e6dfd5 55%,#d8d2c9 80%,#b9b1a6 100%)}
.hero-caption{position:absolute;left:487px;top:392px;width:713px;height:123px;background:rgba(77,102,109,.82);color:var(--white);text-align:right;padding-right:144px;white-space:nowrap}
.hero-caption h1{font-family:'Quicksand',sans-serif;font-weight:500;font-size:32px;line-height:40px;margin-top:16px}
.hero-caption p{font-size:12px;line-height:20px;margin-top:4px;opacity:.95}
.hero-arrow{position:absolute;top:236px;width:40px;height:40px;border-radius:50%;background:var(--white);display:flex;align-items:center;justify-content:center}

/* products */
.tab{position:absolute;top:742px;height:48px;background:var(--tab);color:var(--muted);font-family:'Quicksand',sans-serif;font-size:19px;display:flex;align-items:center;justify-content:center}
.tab.active{background:var(--slate);color:var(--white)}
.tab.active::after{content:"";position:absolute;bottom:-9px;left:50%;margin-left:-9px;border-left:9px solid transparent;border-right:9px solid transparent;border-top:9px solid var(--slate)}
.product{position:absolute;width:297px}
.product-img{width:297px;height:297px;position:relative}
.product-name{text-align:center;font-family:'Quicksand',sans-serif;font-weight:500;font-size:15px;color:var(--slate);margin-top:10px}
.overlay{position:absolute;inset:0;background:rgba(40,44,46,.78)}
.overlay-btn{position:absolute;left:64px;width:169px;height:41px;background:var(--white);color:var(--slate);font-family:'Quicksand',sans-serif;font-weight:500;font-size:15px;display:flex;align-items:center;justify-content:center;border-radius:2px}
.page-dot{position:absolute;top:1550px;width:40px;height:40px;border-radius:50%;background:#e6e7e8;color:#777;font-size:13px;display:flex;align-items:center;justify-content:center}
.page-dot.current{background:var(--slate);color:var(--white)}

/* renovation band */
.reno{position:absolute;left:0;top:1671px;width:1200px;height:480px;background:linear-gradient(90deg,#5a5755 0%,#494848 30%,#5c5b5a 60%,#4a4a4b 85%,#6d6b69 100%);text-align:center;color:var(--white)}
.reno h2{font-family:'Quicksand',sans-serif;font-weight:500;font-size:30px;margin-top:168px}
.reno p{font-family:'Quicksand',sans-serif;font-size:15px;line-height:24px;margin-top:6px}
.btn-light{position:absolute;left:517px;width:166px;height:41px;background:var(--white);color:var(--slate);font-family:'Quicksand',sans-serif;font-weight:500;font-size:15px;display:flex;align-items:center;justify-content:center;border-radius:2px}
.btn-slate{position:absolute;background:var(--slate);color:var(--white);font-family:'Quicksand',sans-serif;font-weight:500;font-size:15px;display:flex;align-items:center;justify-content:center;border-radius:2px}

/* pricing */
.plan{position:absolute;top:2285px;width:297px;height:375px;background:var(--card);text-align:center}
.plan h3{font-family:'Quicksand',sans-serif;font-weight:500;font-size:23px;color:var(--slate);margin-top:26px}
.plan .price{font-family:'Quicksand',sans-serif;font-weight:500;font-size:40px;color:var(--slate);margin-top:4px}
.plan hr{border:0;border-top:1px solid #c9cccd;width:265px;margin:12px auto 14px}
.plan li{list-style:none;font-size:12.5px;height:29px;line-height:29px;color:#666}
.plan li.off{color:#bbb;text-decoration:line-through}
.plan .btn-slate{left:100px;top:302px;width:97px;height:42px}

/* why */
.why{position:absolute;left:0;top:2741px;width:1200px;height:590px;background:var(--band)}
.feature{position:absolute;width:300px;text-align:center}
.feature svg{display:block;margin:0 auto}
.feature h4{font-family:'Quicksand',sans-serif;font-weight:500;font-size:16px;color:var(--slate);line-height:22px;margin-top:14px}
.feature p{font-size:10.5px;line-height:16px;color:#666;margin-top:12px}

/* suppliers */
.supplier{position:absolute;font-family:'Quicksand',sans-serif;font-weight:700;font-size:20px;color:#6c7377;white-space:nowrap;transform:translateX(-50%)}

/* check */
.check{position:absolute;left:0;top:3737px;width:1200px;height:462px;background:var(--band)}
.info-card{position:absolute;top:127px;width:297px;height:253px;background:var(--white);text-align:center}
.info-card .thumb{width:80px;height:80px;border-radius:50%;margin:22px auto 0}
.info-card h4{font-family:'Quicksand',sans-serif;font-weight:500;font-size:20px;color:var(--slate);margin-top:18px}
.info-card p{font-size:11px;line-height:15px;color:#777;margin:6px 20px 0}
.info-card .card-btn{position:absolute;left:13px;top:199px;width:275px;height:37px;background:linear-gradient(#5a7379,#3f565c);color:var(--white);font-size:11px;letter-spacing:.3px;display:flex;align-items:center;justify-content:center}

/* footer */
.site-footer{position:absolute;left:0;top:4446px;width:1200px;height:275px;background:var(--footer);color:var(--footer-text)}
.foot-col{position:absolute;top:52px}
.foot-col h5{font-family:'Quicksand',sans-serif;font-weight:500;font-size:20px;color:var(--white);margin-bottom:12px}
.foot-col li{list-style:none;font-size:10px;height:24px;line-height:24px}
.social{position:absolute;top:88px;width:37px;height:37px;border-radius:50%;background:#3a474d}
.foot-rule{position:absolute;left:143px;top:202px;width:912px;border-top:1px solid #3b484e}
.copyright{position:absolute;top:228px;width:1200px;text-align:center;font-size:11px}
</style>
</head>
<body>

<header class="site-header">
  <div class="brand"><div class="brand-mark"></div><span class="brand-name">Furnvale</span></div>
  <div class="member-btn">
    <svg width="12" height="12" viewBox="0 0 12 12"><path d="M1 6h7M5 3l3 3-3 3M8 1h3v10H8" fill="none" stroke="#4d666d" stroke-width="1.4"/></svg>
    MEMBERSHIP LOGIN
  </div>
  <svg class="header-icon" style="left:983px" width="22" height="22" viewBox="0 0 22 22"><circle cx="9" cy="9" r="6.5" fill="none" stroke="#6e7a7e" stroke-width="2.4"/><path d="M14 14l6 6" stroke="#6e7a7e" stroke-width="3"/></svg>
  <svg class="header-icon" style="left:1033px" width="24" height="22" viewBox="0 0 24 22"><path d="M1 2h4l3 11h12l3-8H6" fill="#6e7a7e" stroke="#6e7a7e" stroke-width="2"/><circle cx="9" cy="18" r="2" fill="#6e7a7e"/><circle cx="19" cy="18" r="2" fill="#6e7a7e"/></svg>
  <nav class="main-nav">
    <span style="left:610px">Home</span>
    <span style="left:689px">Products</span>
    <span style="left:790px">Gallery</span>
    <span style="left:879px">About Us</span>
    <span style="left:980px">Contact Us</span>
  </nav>
</header>

<section class="hero" role="img" aria-label="Smiling consultant in a suit standing beside an open wardrobe with shelves and a hanging rail">
  <div class="hero-arrow" style="left:53px"><svg width="12" height="12" viewBox="0 0 12 12"><path d="M8 2L4 6l4 4" fill="none" stroke="#555" stroke-width="2"/></svg></div>
  <div class="hero-arrow" style="left:1103px"><svg width="12" height="12" viewBox="0 0 12 12"><path d="M4 2l4 4-4 4" fill="none" stroke="#555" stroke-width="2"/></svg></div>
  <div class="hero-caption">
    <h1>Giving your home the new fresh look.</h1>
    <p>We have a choice of delivery options to ensure you receive your goods on time. Give us a call<br>or email us to book a job. You can also visit your nearest Furnvale showroom.</p>
  </div>
</section>

<h2 class="section-title" style="top:688px">Our Products</h2>
<div class="tab active" style="left:143px;width:92px">All</div>
<div class="tab" style="left:244px;width:264px">Sliding Doors</div>
<div class="tab" style="left:517px;width:265px">Wardrobe System</div>
<div class="tab" style="left:790px;width:265px">Storage Space</div>

<div class="product" style="left:143px;top:823px"><div class="product-img" role="img" aria-label="Glass sliding room divider in a bright home office" style="background:linear-gradient(160deg,#e9e7e3,#c9c3bb 60%,#6b4e39)"></div><div class="product-name">Room Divider</div></div>
<div class="product" style="left:451px;top:823px"><div class="product-img" role="img" aria-label="Open walk-in wardrobe with shelves and drawers" style="background:linear-gradient(160deg,#ddd3c6,#b9a791 55%,#8d775f)"></div><div class="product-name">Basic Wardrobe System</div></div>
<div class="product" style="left:758px;top:823px"><div class="product-img" role="img" aria-label="Study nook storage with desk and wall shelf" style="background:linear-gradient(160deg,#d9dadb,#b3b5b6 55%,#6e5a4a)"></div><div class="product-name">Storage Space</div></div>

<div class="product" style="left:143px;top:1183px"><div class="product-img" role="img" aria-label="Dark glass sliding doors" style="background:linear-gradient(160deg,#5b5d5f,#38393b)"><div class="overlay"></div>
  <div class="overlay-btn" style="top:99px">Request a Quote</div>
  <div class="overlay-btn" style="top:156px">Buy Now</div></div><div class="product-name">Glass Sliding Doors</div></div>
<div class="product" style="left:451px;top:1183px"><div class="product-img" role="img" aria-label="Premium wardrobe with hanging shirts and shoe racks" style="background:linear-gradient(160deg,#7a5a42,#4a3a30 55%,#8f8a82)"></div><div class="product-name">Prime Wardrobe System</div></div>
<div class="product" style="left:758px;top:1183px"><div class="product-img" role="img" aria-label="Linen cupboard with white shelves, baskets and folded towels" style="background:linear-gradient(160deg,#eeeae4,#cdbfae 55%,#8a6a4c)"></div><div class="product-name">Linen Cupboard</div></div>

<div class="page-dot" style="left:363px"><svg width="12" height="12" viewBox="0 0 12 12"><path d="M6 2L2 6l4 4M10 2L6 6l4 4" fill="none" stroke="#777" stroke-width="1.5"/></svg></div>
<div class="page-dot current" style="left:427px">1</div>
<div class="page-dot" style="left:475px">2</div>
<div class="page-dot" style="left:522px">3</div>
<div class="page-dot" style="left:570px">4</div>
<div class="page-dot" style="left:618px">5</div>
<div class="abs" style="left:666px;top:1560px;width:64px;font-size:13px;letter-spacing:2px;color:#aaa">·········</div>
<div class="page-dot" style="left:731px">25</div>
<div class="page-dot" style="left:795px"><svg width="12" height="12" viewBox="0 0 12 12"><path d="M2 2l4 4-4 4M6 2l4 4-4 4" fill="none" stroke="#777" stroke-width="1.5"/></svg></div>

<section class="reno" role="img" aria-label="Interior of a dark wardrobe with shoe racks and shelves">
  <h2>A New Home. A Fresh Renovation.</h2>
  <p>Furnvale offers a wide selection of sliding doors, stand-alone wardrobes, walk-in wardrobes,<br>interior shelves, and sliding drawer constructions.</p>
  <div class="btn-light" style="top:264px">Request a Quote</div>
</section>

<h2 class="section-title" style="top:2225px">Pricing</h2>
<div class="plan" style="left:143px"><h3>Basic</h3><div class="price">$15.00</div><hr><ul><li>Curabitur venenatis lacinia ornare</li><li>Etiam mattis augue vehicula</li><li>Aliquam erat volutpat</li><li class="off">Phasellus nisl condimentum vitae</li><li class="off">Nunc sit amet consequat</li></ul><div class="btn-slate">Sign Up</div></div>
<div class="plan" style="left:451px"><h3>Standard</h3><div class="price">$25.00</div><hr><ul><li>Curabitur venenatis lacinia ornare</li><li>Etiam mattis augue vehicula</li><li>Aliquam erat volutpat</li><li>Phasellus nisl condimentum vitae</li><li class="off">Nunc sit amet consequat</li></ul><div class="btn-slate">Sign Up</div></div>
<div class="plan" style="left:758px"><h3>Premium</h3><div class="price">$35.00</div><hr><ul><li>Curabitur venenatis lacinia ornare</li><li>Etiam mattis augue vehicula</li><li>Aliquam erat volutpat</li><li>Phasellus nisl condimentum vitae</li><li>Nunc sit amet consequat</li></ul><div class="btn-slate">Sign Up</div></div>

<section class="why">
  <h2 class="section-title" style="top:73px">Why Choose Furnvale?</h2>
  <div class="feature" style="left:132px;top:145px">
    <svg width="64" height="64" viewBox="0 0 64 64" fill="none" stroke="#4a5256" stroke-width="2"><path d="M10 54L40 24M16 10l38 38-6 6L10 16z"/><circle cx="46" cy="16" r="9"/><path d="M10 54l4 0 0-4"/></svg>
    <h4>Custom Build</h4><p>We custom build the product right here in New Zealand.</p></div>
  <div class="feature" style="left:449px;top:145px">
    <svg width="72" height="64" viewBox="0 0 72 64" fill="none" stroke="#4a5256" stroke-width="2"><path d="M6 24l30-14 30 14-30 14z"/><path d="M6 32l30 14 30-14M6 40l30 14 30-14"/></svg>
    <h4>Wide Range of Selection</h4><p>Cover a range of selections which you can freely choose<br>for your home renovation.</p></div>
  <div class="feature" style="left:766px;top:145px">
    <svg width="64" height="64" viewBox="0 0 64 64" fill="none" stroke="#4a5256" stroke-width="2"><circle cx="32" cy="24" r="18"/><circle cx="32" cy="24" r="11"/><path d="M32 17l2 5h5l-4 3 2 5-5-3-5 3 2-5-4-3h5z"/><path d="M20 38l-6 20 8-4 4 8 6-18M44 38l6 20-8-4-4 8-6-18"/></svg>
    <h4>Product Effectiveness<br>Guarantee</h4><p>Each slider has 4 wheels on top and 2 wheels at the<br>bottom.</p></div>
  <div class="feature" style="left:132px;top:342px">
    <svg width="72" height="68" viewBox="0 0 72 68" fill="none" stroke="#4a5256" stroke-width="2"><rect x="4" y="4" width="64" height="60"/><path d="M4 56h64M24 4v52M48 4v52M28 20h16M28 36h16"/></svg>
    <h4>Premium Materials and<br>Quality</h4><p>Extremely smooth, World class quality made from<br>Aluminum, designed to last a life time.</p></div>
  <div class="feature" style="left:449px;top:342px">
    <svg width="68" height="68" viewBox="0 0 68 68" fill="none" stroke="#4a5256" stroke-width="2"><circle cx="34" cy="34" r="28"/><path d="M12 22c8 2 10 10 18 8s4-14 12-16M36 62c-2-10 8-12 6-22s14-6 20-4"/><circle cx="46" cy="44" r="7"/></svg>
    <h4>Multiple Showrooms &amp; Friendly<br>Staffs</h4><p>You can visit our showrooms to view our products or<br>talk to us for advice.</p></div>
  <div class="feature" style="left:766px;top:342px">
    <svg width="68" height="68" viewBox="0 0 68 68" fill="none" stroke="#4a5256" stroke-width="2"><circle cx="34" cy="34" r="28"/><path d="M20 40l10-14c2-3 6-3 8 0l10 8M30 26l4-8c1-3 5-2 5 1l-1 7M48 34l6 8"/></svg>
    <h4>Satisfaction Guarantee</h4><p>We guarantee that our products will fit into your home<br>perfectly. Smooth, Quiet and Most importantly - Beauti-<br>ful.</p></div>
</section>

<h2 class="section-title" style="top:3407px">Proudly Supplier</h2>
<div class="supplier" style="left:209px;top:3500px">Kerrow Build</div>
<div class="supplier" style="left:368px;top:3500px">Vantage Boards</div>
<div class="supplier" style="left:522px;top:3500px">Oakridge</div>
<div class="supplier" style="left:678px;top:3500px">Lumena</div>
<div class="supplier" style="left:834px;top:3500px">Formwell</div>
<div class="supplier" style="left:990px;top:3500px">Quartzline</div>
<div class="supplier" style="left:300px;top:3610px">Brenner</div>
<div class="supplier" style="left:454px;top:3610px">Kessler</div>
<div class="supplier" style="left:610px;top:3610px">Halvo</div>
<div class="supplier" style="left:768px;top:3610px">Decorva</div>
<div class="supplier" style="left:923px;top:3610px">Marco Vienti</div>

<section class="check">
  <h2 class="section-title" style="top:73px">Check these out.</h2>
  <div class="info-card" style="left:143px"><div class="thumb" role="img" aria-label="Wardrobe interior guide photo" style="background:radial-gradient(#d8d8d6,#8f9091)"></div><h4>Our Buyer Guide</h4><p>We will guide you on how to select the right product for your home.</p><div class="card-btn">VIEW OUR GUIDE</div></div>
  <div class="info-card" style="left:451px"><div class="thumb" role="img" aria-label="Brochure cover photo of a dark wardrobe" style="background:radial-gradient(#6f6b68,#2e2d2c)"></div><h4>Our 2019 Brochure</h4><p>Download our brochure to check out our latest products.</p><div class="card-btn">DOWNLOAD BROCHURE</div></div>
  <div class="info-card" style="left:758px"><div class="thumb" role="img" aria-label="White shelving unit photo" style="background:radial-gradient(#eeeeec,#9c9d9e)"></div><h4>Tradies Offer</h4><p>Call us today to enquire about the best deal we can offer.</p><div class="card-btn">CALL US NOW!</div></div>
</section>

<h2 class="section-title" style="top:4274px">Looking to renovate your wardrobe?</h2>
<div class="btn-slate" style="left:517px;top:4323px;width:166px;height:43px">Request a Quote</div>

<footer class="site-footer">
  <div class="foot-col" style="left:143px"><h5>Quick Links</h5><ul><li>Home</li><li>Products</li><li>Gallery</li><li>Buyer's Guide</li></ul></div>
  <div class="foot-col" style="left:359px"><h5>Products</h5><ul><li>Doors</li><li>Wardrobe System</li><li>Storage Space</li><li>Accessories</li></ul></div>
  <div class="foot-col" style="left:583px"><h5>Our Branches</h5><ul><li>Northbay Showroom - 09 555 0142</li><li>Riverton Showroom - 07 555 0187</li></ul></div>
  <div class="foot-col" style="left:868px"><h5>Follow us on</h5></div>
  <div class="social" style="left:873px" aria-label="Social link"></div>
  <div class="social" style="left:920px" aria-label="Social link"></div>
  <div class="social" style="left:968px" aria-label="Social link"></div>
  <div class="social" style="left:1015px" aria-label="Social link"></div>
  <div class="foot-rule"></div>
  <div class="copyright">Copyright © 2019 Furnvale. All rights reserved.</div>
</footer>

</body>
</html>
```